IT Services

We come to you
Only $49/hr
No contract, no monthly fee
Software engineer on staff
remote assistance or visit in your office

On the back of the card I want to list services.

- Server setup
- Network troubleshooting
- Printer setup
- Secure backup setup
- Software installation
- Wireless network setup
- Wired network setup
- Disaster recovery
- Website management
- Any other technology related support
- Email setup
- HIPAA compliance review and setup
Updates

the URL is: GEARFIXPRO.ZONE please use it on the card

On the card we need to mention "Connect remotely to address your IT issues" if there is enough room as well as "we go to you"

Industry/Entity Type

Printer

Contact Information for Business Card

I want a busoiness card to offer my services to doctor offices, it can be dentists, Otamatry, and other professions. I provide the following service. My plan is to go to their office and drop off my card. I don't want them to forget about it that is why I am paying for the design. I like hand writing design formats.

```html
<!DOCTYPE html>
<html lang="en">
<head>
<meta charset="utf-8">
<title>GEARFIXPRO.ZONE — Business Card</title>
<link href="https://fonts.googleapis.com/css2?family=Nothing+You+Could+Do&family=Roboto:wght@400&display=swap" rel="stylesheet">
<style>
  :root {
    --bg: #ece9e4;
    --navy: #0f3466;
    --navy-deep: #0a2650;
    --navy-light: #1d4d86;
    --red: #d8344a;
    --white: #ffffff;
    --paper: #f7f7f6;
    --ink: #1b3c6e;
    --hand: "Nothing You Could Do", cursive;
    --sans: "Roboto", Arial, sans-serif;
  }
  * { box-sizing: border-box; margin: 0; padding: 0; }
  html, body { width: 1200px; height: 1023px; overflow: hidden; }
  body { background: var(--bg); position: relative; font-family: var(--sans); }

  .card {
    position: absolute;
    width: 680px;
    height: 388px;
    border-radius: 4px;
    overflow: hidden;
    box-shadow: 0 10px 28px rgba(0,0,0,.22);
  }

  /* Front */
  .card--front { left: 40px; top: 60px; background: var(--paper); }
  .front__top {
    position: absolute; left: 0; top: 0; width: 100%; height: 176px;
    display: flex; flex-direction: column; align-items: center; justify-content: center; gap: 20px;
  }
  .brand__name { font-family: var(--sans); font-weight: 400; color: var(--ink); font-size: 36px; letter-spacing: .5px; }
  .tagline { font-family: var(--hand); color: var(--ink); font-size: 20px; }
  .front__band {
    position: absolute; left: 0; top: 176px; width: 100%; height: 212px;
    background: linear-gradient(160deg, var(--navy-light), var(--navy) 45%, var(--navy-deep));
  }
  .rule { position: absolute; height: 3px; background: var(--red); }
  .rule--top { right: 0; top: 0; width: 250px; }
  .rule--bottom { left: 0; bottom: 36px; width: 250px; }
  .contact { position: absolute; left: 0; width: 100%; top: 38px; text-align: center; color: var(--white); font-family: var(--hand); }
  .contact__name { font-size: 30px; }
  .contact__phone { font-size: 42px; letter-spacing: 4px; margin-top: 12px; }

  /* Back */
  .card--back {
    left: 480px; top: 575px;
    background: linear-gradient(160deg, var(--navy-light), var(--navy) 45%, var(--navy-deep));
    color: var(--white);
  }
  .back__url {
    position: absolute; left: 24px; top: 0; height: 100%; width: 20px;
    display: flex; align-items: center; justify-content: center;
  }
  .back__url span {
    transform: rotate(-90deg); white-space: nowrap;
    font-family: var(--sans); font-size: 13px; letter-spacing: 3px;
  }
  .back__line { position: absolute; left: 56px; top: 30px; bottom: 30px; width: 2px; background: var(--white); opacity: .9; }
  .services {
    position: absolute; left: 80px; right: 22px; top: 36px;
    list-style: none; font-family: var(--hand); font-size: 16px; line-height: 36px;
  }
  .services li { white-space: nowrap; }
  .services span + span { margin-left: 10px; }
  .services span::before { content: "• "; }
  .back__brand { position: absolute; right: 28px; bottom: 26px; }
  .back__brand .brand__name { color: var(--white); font-size: 26px; }
</style>
</head>
<body>
  <section class="card card--front" aria-label="Business card front">
    <div class="front__top">
      <span class="brand__name">GEARFIXPRO.ZONE</span>
      <p class="tagline">Connect remotely to address your IT issues. we go to you</p>
    </div>
    <div class="front__band">
      <span class="rule rule--top"></span>
      <div class="contact">
        <p class="contact__name">Dean Holloway</p>
        <p class="contact__phone">1-800-555-0142</p>
      </div>
      <span class="rule rule--bottom"></span>
    </div>
  </section>

  <section class="card card--back" aria-label="Business card back">
    <div class="back__url"><span>www.gearfixpro.zone</span></div>
    <span class="back__line"></span>
    <ul class="services">
      <li><span>Server setup</span><span>Network troubleshooting</span><span>Printer setup</span></li>
      <li><span>Secure backup setup</span><span>Software installation</span><span>Wireless network setup</span></li>
      <li><span>Wired network setup</span><span>Disaster recovery</span><span>Website management</span></li>
      <li><span>Any other technology related support</span><span>Email setup</span></li>
      <li><span>HIPAA compliance review and setup</span></li>
    </ul>
    <div class="back__brand">
      <span class="brand__name">GEARFIXPRO.ZONE</span>
    </div>
  </section>
</body>
</html>
```